Attorney Business Card

I need a business card that looks professional yet modern. I am an Attorney. , I need a professional yet modern business card for my law practice. My logo and information have been uploaded. , I need a business card that looks professional yet modern. I am an Attorney. , I need a professional yet modern business card for my law practice. My logo and information have been uploaded.

Industry/Entity Type

Business

Requirements
Must have
• My logo which has been uploaded , my logo , My logo which has been uploaded , my logo

```html
<!DOCTYPE html>
<html lang="en">
<head>
<meta charset="utf-8">
<title>Harwell Law Firm – Business Card</title>
<link rel="stylesheet" href="https://fonts.googleapis.com/css2?family=Exo+2:wght@400;600;700&family=Open+Sans:wght@400;700&display=swap">
<style>
  :root {
    --backdrop-light: #f1f1f1;
    --backdrop-dark: #cfcfcf;
    --card-dark: #1d1312;
    --leather-light: #5a4028;
    --leather-mid: #45301d;
    --leather-dark: #2e1f12;
    --accent-orange: #f39a1e;
    --accent-blue: #1f9fd8;
    --text-white: #f4f1ec;
  }
  * { margin: 0; padding: 0; box-sizing: border-box; }
  html, body { width: 1200px; height: 798px; overflow: hidden; }
  body {
    background: radial-gradient(ellipse at 40% 30%, var(--backdrop-light), var(--backdrop-dark));
    display: flex;
    align-items: center;
    justify-content: center;
    gap: 40px;
    font-family: "Open Sans", sans-serif;
  }
  .card {
    position: relative;
    width: 540px;
    height: 309px;
    border-radius: 4px;
    overflow: hidden;
    box-shadow: 0 10px 24px rgba(0,0,0,0.22);
  }

  /* Back side */
  .card-back {
    background: var(--card-dark);
    display: flex;
    flex-direction: column;
    align-items: center;
    justify-content: center;
    gap: 14px;
  }
  .firm-mark {
    width: 62px;
    height: 62px;
    border: 4px solid var(--accent-blue);
    border-radius: 50%;
  }
  .firm-name {
    font-family: "Exo 2", sans-serif;
    font-weight: 600;
    color: var(--accent-blue);
    font-size: 34px;
    letter-spacing: 2px;
    text-transform: uppercase;
    text-align: center;
    line-height: 1.1;
  }

  /* Front side */
  .card-front { color: var(--text-white); }
  .leather-surface {
    position: absolute;
    inset: 0;
    background: radial-gradient(ellipse at 50% 45%, var(--leather-light), var(--leather-mid) 55%, var(--leather-dark));
  }
  .front-content { position: absolute; inset: 0; }
  .attorney-name {
    position: absolute;
    left: 34px; top: 42px;
    font-family: "Exo 2", sans-serif;
    font-weight: 700;
    font-size: 22px;
    letter-spacing: 1.5px;
    color: var(--accent-orange);
    text-transform: uppercase;
  }
  .attorney-title {
    position: absolute;
    left: 34px; top: 72px;
    font-size: 18px;
    color: var(--text-white);
  }
  .front-logo {
    position: absolute;
    right: 26px; top: 26px;
    display: flex;
    flex-direction: column;
    align-items: center;
    gap: 6px;
  }
  .front-logo .firm-mark { width: 44px; height: 44px; border-width: 3px; }
  .front-logo .firm-name { font-size: 15px; letter-spacing: 1px; }
  .contact-phones {
    position: absolute;
    left: 34px; top: 160px;
    list-style: none;
    font-weight: 700;
    font-size: 16px;
    line-height: 1.45;
  }
  .contact-phones .label { display: inline-block; width: 46px; }
  .office-address {
    position: absolute;
    left: 34px; bottom: 26px;
    font-style: normal;
    font-family: "Exo 2", sans-serif;
    font-size: 15px;
    line-height: 1.55;
    color: var(--accent-orange);
    text-transform: uppercase;
  }
  .online-contact {
    position: absolute;
    right: 26px; top: 150px;
    text-align: right;
    font-size: 12.5px;
    line-height: 1.6;
    color: var(--accent-orange);
  }
</style>
</head>
<body>
  <section class="card card-back" aria-label="Card back">
    <div class="firm-mark"></div>
    <div class="firm-name">Harwell Law Firm</div>
  </section>

  <section class="card card-front" aria-label="Card front">
    <div class="leather-surface" role="img" aria-label="Dark brown leather texture background"></div>
    <div class="front-content">
      <h1 class="attorney-name">Daniel Harwell, Esq.</h1>
      <p class="attorney-title">Attorney At LAW</p>
      <div class="front-logo">
        <div class="firm-mark"></div>
        <div class="firm-name">Harwell Law Firm</div>
      </div>
      <ul class="contact-phones">
        <li><span class="label">Tele</span>: 555.204.3100</li>
        <li><span class="label">Fax</span>: 555.204.3190</li>
        <li><span class="label">Mob</span>: 555.318.7742</li>
      </ul>
      <address class="office-address">
        1820 Crestview Blvd Suite 400<br>
        Westbrook, CA 90000
      </address>
      <div class="online-contact">
        daniel@hwfirm.com<br>
        www.hwfirm.com
      </div>
    </div>
  </section>
</body>
</html>
```